***PLASTIC*** Business Card Design

1 sided business card design
The card will be screen printed on plastic, so colour and fonts must be strong.

Must use the colours in the logo eps attached (Black/Ivory/White). Other colour(s) can be added.

Four (4) examples of how the logo can be printed are included in the logo eps attached.

The business card should highlight the logo. The card will be given to architects, interior designers and builders. It should look sophisticated but also innovative.

Do not cover the whole card with colour as it is important than some of the frosted plastic card is visible.

Be creative.

Target Market(s)

architects, interior designers and builders and wealthy home owners

Industry/Entity Type

Plastic

Requirements
Must have
• Must use the colours in the logo eps attached (Black/Ivory/White). Other colour(s) can be added if necessary.

The font is Square721 ExBT but has been a little thickened. It is not essential that you use this font. The name should be a stronger version of the font than other details.

The card will be printed on PVC - see http://www.voltrap.com.au/pricelistbcardsplastic.php

Final artwork must be print ready. You must use the printing spec at http://www.voltrap.com.au/2011%20PVC-TW.pdf

The actual details to be typeset ono the card are:

Dorian Welch

Mobile: 0412 806133
email: info@halcoworks.com.au
www.halcoworks.com.au

PO Box 53, Altona, Vic 3018

Plastering | Rendering | Cornicing

```html
<!DOCTYPE html>
<html lang="en">
<head>
<meta charset="utf-8">
<title>Halco Works – Business Card</title>
<link rel="stylesheet" href="https://fonts.googleapis.com/css2?family=Questrial&display=swap">
<style>
  :root {
    --page-bg: #ffffff;
    --card-frost: #ffffff;
    --card-edge: #d6d6d6;
    --ink: #111111;
    --panel: #000000;
    --ivory: #ffffff;
  }
  html, body {
    margin: 0;
    padding: 0;
    overflow: hidden;
  }
  body {
    width: 1200px;
    height: 720px;
    background: var(--page-bg);
    position: relative;
    font-family: "Questrial", "Century Gothic", sans-serif;
  }
  .card {
    position: absolute;
    left: 343px;
    top: 199px;
    width: 487px;
    height: 291px;
    box-sizing: border-box;
    border: 1px solid var(--card-edge);
    border-radius: 16px;
    background: var(--card-frost);
    overflow: hidden;
    color: var(--ink);
  }
  .contact {
    position: absolute;
    left: 11px;
    top: 140px;
    margin: 0;
    font-size: 13.5px;
    line-height: 20px;
    font-style: normal;
    letter-spacing: -0.1px;
  }
  .services {
    position: absolute;
    left: 11px;
    top: 253px;
    margin: 0;
    font-size: 13.5px;
    letter-spacing: -0.1px;
    white-space: nowrap;
  }
  .services .divider {
    padding: 0 4px;
  }
  .brand-panel {
    position: absolute;
    left: 226px;
    top: -1px;
    width: 220px;
    height: 293px;
    background: var(--panel);
    color: var(--ivory);
  }
  .brand-name {
    position: absolute;
    left: 0;
    right: 0;
    top: 22px;
    margin: 0;
    text-align: center;
    font-weight: 400;
    line-height: 1;
  }
  .brand-name .word-main {
    display: block;
    font-size: 42px;
    letter-spacing: 4px;
  }
  .brand-name .word-sub {
    display: block;
    margin-top: 6px;
    font-size: 18px;
    letter-spacing: 7px;
    padding-left: 7px;
  }
  .person-name {
    position: absolute;
    left: 0;
    right: 0;
    top: 140px;
    margin: 0;
    text-align: center;
    font-size: 16.5px;
    font-weight: 400;
  }
  .web-strip {
    position: absolute;
    left: 446px;
    top: 0;
    width: 41px;
    height: 291px;
  }
  .web-address {
    position: absolute;
    left: 50%;
    top: 145px;
    transform: translate(-50%, -50%) rotate(-90deg);
    white-space: nowrap;
    font-size: 17px;
    letter-spacing: 0.3px;
  }
</style>
</head>
<body>
  <div class="card">
    <address class="contact">
      0412 806133<br>
      info@halcoworks.com.au<br>
      PO Box 53, Brackley, Vic 3921
    </address>
    <p class="services">Plastering<span class="divider">|</span>Rendering<span class="divider">|</span>Cornicing</p>

    <div class="brand-panel">
      <h1 class="brand-name">
        <span class="word-main">HALCO</span>
        <span class="word-sub">WORKS</span>
      </h1>
      <p class="person-name">Dorian Welch</p>
    </div>

    <div class="web-strip">
      <span class="web-address">www.halcoworks.com.au</span>
    </div>
  </div>
</body>
</html>
```